Business Card Design of an established Waste Management, Plastic Recycling and Renewable Energy Comp

We are looking for business card design for plastic card with holograms (Very similar to credit card). I will provide our logo (Quillbys). So the name on the business card will be our logo )Quillbys) + Environmental next to it, so it will read Quillbys Environmental. The font for Environmental does not to be the same as the font of the logo. The holograms will be used to display ISO14001 Certified (In normal credit card, normally on the holograms, they show orbis or plex). I will post the design requirements from the card printing company very shortly to make sure they can use the design for the plastic card.

Target Market(s)

Companies, Government Organizations, Corporations.

Industry/Entity Type

Business

Contact Information for Business Card

Motto (Under the logo): Let's Do It Right
Name: Bertolomeus Kesslani; Position: Business Manager; Address: Fernwick Landfill & Recycling Facility, Tallowmere Rd, Fernwick Downs, WA 6122; Ph: +61 8 6100 4213; Mob: +61 400 917 358; E: Bertram@quillbysenvironmental.com

Requirements
Must have
• Business Names: Quillbys Logo + Environmental word after the logo.
• Motto (Under the logo): Let's Do It Right
• All the Business Card Details above.
• Hologram Logo on the lower right corner which says: ISO 14001 Certified.
• Please remember the design will be printed on plastic card Not paper. The plastic crad is the same as credit card. Hope this helps. Thank You

```html
<!DOCTYPE html>
<html lang="en">
<head>
<meta charset="utf-8">
<title>Quillbys Environmental – Business Card</title>
<link rel="stylesheet" href="https://fonts.googleapis.com/css2?family=Open+Sans:wght@400;600;700&family=Lato:wght@700&display=swap">
<style>
  :root {
    --page: #e9ecf0;
    --blue-light: #4d9bd6;
    --blue-mid: #2a78c2;
    --blue-deep: #174e8f;
    --panel-dark: #2c3036;
    --card-grey: #55585d;
    --card-grey-deep: #2f3237;
    --text-white: #f3f5f8;
    --text-soft: #d6dbe4;
    --name-blue: #1f6fd0;
    --motto: #a9b3e6;
    --silver: #c9d0da;
  }
  * { margin: 0; padding: 0; box-sizing: border-box; }
  html, body { width: 800px; height: 1200px; overflow: hidden; }
  body {
    background: var(--page);
    font-family: "Open Sans", Arial, sans-serif;
    position: relative;
  }
  .card {
    position: absolute;
    left: 90px;
    width: 620px;
    height: 354px;
    border-radius: 4px;
    overflow: hidden;
    box-shadow: 0 10px 30px rgba(20, 30, 50, 0.18);
  }

  /* Front */
  .card-front {
    top: 150px;
    background: linear-gradient(115deg, var(--blue-light) 0%, var(--blue-mid) 45%, var(--blue-deep) 100%);
  }
  .front-sheen {
    position: absolute;
    right: 0; top: 0;
    width: 250px; height: 60px;
    background: linear-gradient(90deg, rgba(255,255,255,0) 0%, rgba(236,240,246,0.75) 60%, rgba(236,240,246,0.9) 100%);
  }
  .profile-panel {
    position: absolute;
    left: 304px; top: 49px;
    width: 264px; height: 250px;
    background: var(--panel-dark);
    border-radius: 125px 6px 6px 125px;
  }
  .brand {
    position: absolute;
    display: flex; align-items: center;
  }
  .brand-mark {
    border-radius: 50%;
    flex: none;
  }
  .brand-name { font-weight: 700; line-height: 1; white-space: nowrap; }
  .card-front .brand { left: 27px; top: 48px; gap: 9px; }
  .card-front .brand-mark { width: 30px; height: 30px; background: var(--text-white); }
  .card-front .brand-name { font-size: 20px; color: #33363b; }

  .contact {
    position: absolute;
    left: 27px;
    display: flex; align-items: center; gap: 9px;
    font-size: 15px; color: var(--text-soft);
    white-space: nowrap;
  }
  .contact svg { width: 13px; height: 13px; flex: none; }
  .contact-web { top: 166px; }
  .contact-phone { top: 268px; }
  .contact-mobile { top: 288px; }
  .contact-email { top: 308px; }

  .cert-seal {
    position: absolute;
    border-radius: 50%;
    background: radial-gradient(circle at 40% 35%, #e6ebf2 0%, var(--silver) 55%, #9aa6b6 100%);
  }
  .cert-seal-left {
    left: 27px; top: 194px;
    width: 68px; height: 68px;
    opacity: 0.75;
  }
  .cert-hologram {
    right: 16px; bottom: 12px;
    width: 44px; height: 44px;
    opacity: 0.9;
  }

  .holder {
    position: absolute;
    right: 66px; top: 156px;
    text-align: right;
  }
  .holder-name { font-size: 18px; font-weight: 700; color: var(--name-blue); line-height: 1.2; white-space: nowrap; }
  .holder-role { font-size: 14px; color: var(--text-soft); line-height: 1.35; }

  /* Back */
  .card-back {
    top: 720px;
    background: linear-gradient(180deg, var(--card-grey) 0%, #44474c 50%, var(--card-grey-deep) 100%);
    text-align: center;
  }
  .card-back .brand { left: 0; right: 0; top: 100px; justify-content: center; gap: 12px; }
  .card-back .brand-mark { width: 44px; height: 44px; background: var(--name-blue); }
  .card-back .brand-name { font-size: 36px; color: var(--text-white); }
  .motto {
    position: absolute; left: 0; right: 0; top: 190px;
    font-family: "Lato", Arial, sans-serif;
    font-weight: 700; font-size: 14px; letter-spacing: 0.5px;
    color: var(--motto);
  }
  .address {
    position: absolute; left: 0; right: 0; top: 234px;
    font-size: 15px; line-height: 20px; color: var(--text-soft);
    font-style: normal;
  }
</style>
</head>
<body>

<section class="card card-front" aria-label="Card front">
  <div class="front-sheen"></div>
  <div class="profile-panel"></div>

  <div class="brand">
    <span class="brand-mark"></span>
    <span class="brand-name">Quillbys Environmental</span>
  </div>

  <div class="contact contact-web">
    <svg viewBox="0 0 14 14" fill="none" stroke="#c7d3e6" stroke-width="1.2"><circle cx="7" cy="7" r="6"/><ellipse cx="7" cy="7" rx="2.6" ry="6"/><path d="M1 7h12M2 4h10M2 10h10"/></svg>
    <span>www.quillbysgroup.com</span>
  </div>

  <div class="cert-seal cert-seal-left" role="img" aria-label="ISO 14001 certified seal"></div>

  <div class="contact contact-phone">
    <svg viewBox="0 0 14 14" fill="#c7d3e6"><path d="M3 1l2.2 2.6-1.2 1.6c.8 1.8 2 3 3.8 3.8l1.6-1.2L12 10l-1.2 2.4C6 12.4 1.6 8 1.6 3.2z"/></svg>
    <span>+61 8 6100 4213</span>
  </div>
  <div class="contact contact-mobile">
    <svg viewBox="0 0 14 14" fill="none" stroke="#c7d3e6" stroke-width="1.3"><rect x="3.5" y="1" width="7" height="12" rx="1.2"/><path d="M6 11h2"/></svg>
    <span>+61 400 917 358</span>
  </div>
  <div class="contact contact-email">
    <svg viewBox="0 0 14 14" fill="none" stroke="#c7d3e6" stroke-width="1.2"><rect x="1" y="3" width="12" height="8" rx="1"/><path d="M1 3l6 5 6-5"/></svg>
    <span>Bertram@quillbysenvironmental.com</span>
  </div>

  <div class="holder">
    <p class="holder-name">Bertolomeus Kesslani</p>
    <p class="holder-role">Business Manager</p>
  </div>

  <div class="cert-seal cert-hologram" role="img" aria-label="ISO 14001 certified hologram"></div>
</section>

<section class="card card-back" aria-label="Card back">
  <div class="brand">
    <span class="brand-mark"></span>
    <span class="brand-name">Quillbys Environmental</span>
  </div>
  <p class="motto">LET’S DO IT RIGHT</p>
  <address class="address">
    Fernwick Landfill &amp; Recycling Facility<br>
    Tallowmere Rd, Fernwick Downs, WA 6122
  </address>
</section>

</body>
</html>
```